Clear tides coaching programme

I need a flyer designed to promote my coaching programme. The programme is designed to help people who are feeling a bit lost in their life, looking for new possiblities or that they want more focus in their goals. It is an intensive programme designed to help people achieve real change in their lives. It is a premium product targeted at senior managers, directors and business leaders. I care passionately about helping people achieve their potential. I would like the design to fit with the logo (attached) and I've drafted the content (also attached). I would like it to be A5 and affordable to print - so not full colour.

```html
<!DOCTYPE html>
<html lang="en">
<head>
<meta charset="utf-8">
<title>Clear Tides Coaching Programme</title>
<link rel="stylesheet" href="https://fonts.googleapis.com/css2?family=Didact+Gothic&family=Montserrat:wght@700&display=swap">
<style>
  :root {
    --purple: #4a3590;
    --purple-soft: #b9aed8;
    --teal: #2cb39f;
    --ink: #2b2b2b;
    --paper: #ffffff;
  }
  html, body {
    margin: 0;
    padding: 0;
    width: 846px;
    height: 1200px;
    overflow: hidden;
    background: var(--paper);
  }
  .flyer {
    position: relative;
    width: 846px;
    height: 1200px;
    box-sizing: border-box;
    border: 10px solid var(--purple);
    background: var(--paper);
    font-family: "Didact Gothic", "Century Gothic", sans-serif;
    color: var(--ink);
    overflow: hidden;
  }
  .flyer > * { position: absolute; z-index: 1; margin: 0; }
  .brand {
    left: 120px;
    top: 30px;
    width: 200px;
    text-align: center;
  }
  .brand-mark {
    display: block;
    width: 130px;
    height: 130px;
    margin: 0 auto 12px;
    border-radius: 50%;
    background: var(--teal);
  }
  .brand-name {
    font-size: 34px;
    line-height: 1.05;
    color: var(--purple);
  }
  .quote {
    left: 434px;
    top: 100px;
    width: 350px;
    font-style: italic;
    font-size: 19px;
    line-height: 30px;
    color: var(--teal);
  }
  .quote-author {
    right: 30px;
    top: 196px;
    font-size: 19px;
  }
  .question-heading {
    left: 44px;
    top: 306px;
    font-family: "Montserrat", sans-serif;
    font-weight: 700;
    font-size: 23px;
    color: var(--teal);
  }
  .question-list {
    left: 44px;
    top: 342px;
    padding: 0;
    list-style: none;
    font-size: 24px;
  }
  .question-list li {
    position: relative;
    padding-left: 28px;
    height: 41px;
    line-height: 34px;
  }
  .question-list li::before {
    content: "";
    position: absolute;
    left: 4px;
    top: 12px;
    width: 11px;
    height: 11px;
    background: var(--teal);
    transform: rotate(45deg);
  }
  .call-out {
    left: 44px;
    top: 506px;
    font-size: 27px;
    letter-spacing: 0.3px;
  }
  .body-copy {
    left: 31px;
    width: 770px;
    font-size: 20px;
    line-height: 30px;
    text-align: justify;
  }
  .intro { top: 580px; }
  .programme { top: 664px; }
  .benefit { top: 832px; }
  .why-heading {
    left: 31px;
    top: 914px;
    font-family: "Montserrat", sans-serif;
    font-weight: 700;
    font-size: 19px;
  }
  .why { top: 948px; }
  .closing {
    left: 31px;
    top: 1086px;
    width: 770px;
    font-size: 20px;
    line-height: 29px;
    text-align: center;
  }
  .backdrop-mark {
    right: -10px;
    bottom: -30px;
    width: 330px;
    height: 350px;
    border-radius: 50%;
    background: var(--purple-soft);
    opacity: 0.35;
    z-index: 0;
  }
</style>
</head>
<body>
  <main class="flyer">
    <div class="backdrop-mark" role="img" aria-label="Faint brand backdrop"></div>

    <header class="brand">
      <span class="brand-mark"></span>
      <div class="brand-name">Reaching Further</div>
    </header>

    <p class="quote">“The secret of change is to focus all of your energy not on fighting the old, but on building the new”.</p>
    <span class="quote-author">Marlow Ashby</span>

    <h2 class="question-heading">ARE YOU:</h2>
    <ul class="question-list">
      <li>Fed up but unsure how to move on?</li>
      <li>Finding it hard to focus?</li>
      <li>Dreaming of what could come next in your life?</li>
      <li>Looking for new opportunities and possibilities?</li>
    </ul>
    <p class="call-out">Then its time to move on.</p>

    <p class="body-copy intro">So make that first step towards a happier life and take up your own, personally tailored ‘Clear Tides’ coaching journey.</p>

    <p class="body-copy programme">This programme consists of 6 face to face coaching sessions, each 90 minutes long and carefully designed around you, your needs and goals. You will also benefit from free email support in between your sessions, development feedback, recommended resources to support your journey and a bespoke action plan.</p>

    <p class="body-copy benefit">This programme will help you achieve your goals and increase your satisfaction with your work and home life.</p>

    <h3 class="why-heading">Why work with me?</h3>
    <p class="body-copy why">I’m a coach and transformational leader with a decade of experience in delivering better results for individuals, organisations and customers. I’m passionate about helping people achieve their potential and find new possibilities.</p>

    <p class="closing">So, take the first step today towards your own 'Clear Tides' and book a free<br>15 minute phone or video consultation by emailing me at<br>hello@reachingfurther.net</p>
  </main>
</body>
</html>
```